new business card, with new logo. Looking for full design

I would like to have a graphic designer/artist create a high standard, premium business logo and business card design that I can either use to print on my own or have printed through them as well. Also, would be nice if I could customize with new employee names and info afterwards. Also, though I don't have a logo, something that matches the theme here https://veridanstrategy.com/ as well as incorporates the letter "M" is what I am currently thinking. Thanks!

Target Market(s)

High end corporate executives

Industry/Entity Type

Economics

Contact Information for Business Card

Dr. Tomas Ruelle-Brandt
Principal Advisor
TRB@VeridanStrategy.com
other contact/website details from here: https://veridanstrategy.com/

Logo Text

Veridan Strategy Group

```html
<!DOCTYPE html>
<html lang="en">
<head>
<meta charset="utf-8">
<title>Veridan Strategy Group — Business Card</title>
<link href="https://fonts.googleapis.com/css2?family=EB+Garamond:wght@400;500&display=swap" rel="stylesheet">
<style>
  :root {
    --stage: #1f1f1f;
    --card: #5f5248;
    --rose: #c48e80;
    --light: #e9e3de;
    --rule: #8a7a6e;
    --accent: #3aa5dd;
  }
  * { margin: 0; padding: 0; box-sizing: border-box; }
  html, body { width: 1200px; height: 1015px; overflow: hidden; background: var(--stage); }
  body {
    font-family: "EB Garamond", Georgia, serif;
    display: flex; flex-direction: column; align-items: center; justify-content: center; gap: 56px;
  }
  .card {
    position: relative; width: 700px; height: 400px; background: var(--card);
    box-shadow: 0 10px 30px rgba(0,0,0,.55);
  }
  .brand { display: flex; align-items: center; gap: 22px; color: var(--rose); }
  .brand-square { width: 46px; height: 46px; border: 2px solid var(--rose); flex: none; }
  .brand-name { font-size: 44px; font-weight: 400; letter-spacing: 1px; white-space: nowrap; }

  .card-front .brand { position: absolute; left: 90px; top: 120px; }
  .front-rule { position: absolute; left: 200px; right: 70px; top: 246px; height: 1px; background: var(--rule); }
  .front-dot {
    position: absolute; left: 426px; top: 232px; width: 28px; height: 28px; border-radius: 50%;
    background: var(--accent); box-shadow: 0 0 0 8px var(--card);
  }

  .card-back .brand { position: absolute; left: 60px; top: 50px; }
  .card-back .brand-name { font-size: 46px; }
  .contact { position: absolute; left: 128px; top: 140px; color: var(--light); }
  .person-name { color: var(--rose); font-size: 24px; font-weight: 500; letter-spacing: 1.5px; text-transform: uppercase; line-height: 1; }
  .person-title { font-size: 19px; margin-top: 2px; }
  .address { font-size: 19px; line-height: 1.2; margin-top: 16px; }
  .links { list-style: none; margin-top: 18px; font-size: 19px; line-height: 1.35; }
  .links li { display: flex; align-items: center; gap: 12px; }
  .links svg { width: 18px; height: 18px; flex: none; stroke: var(--rose); fill: none; stroke-width: 1.6; }
</style>
</head>
<body>
  <section class="card card-front" aria-label="Card front">
    <div class="brand">
      <span class="brand-square"></span>
      <span class="brand-name">Veridan Strategy Group</span>
    </div>
    <div class="front-rule"></div>
    <span class="front-dot"></span>
  </section>

  <section class="card card-back" aria-label="Card back">
    <div class="brand">
      <span class="brand-square"></span>
      <span class="brand-name">Veridan Strategy Group</span>
    </div>
    <div class="contact">
      <p class="person-name">Adrian Calloway</p>
      <p class="person-title">Managing Director</p>
      <p class="address">418 Larkin Ave Suite 210<br>Riverton, MD 20914</p>
      <ul class="links">
        <li><svg viewBox="0 0 20 20"><path d="M5 2l3 4-2 2c1 2.5 3.5 5 6 6l2-2 4 3-2 3C9 17 3 11 2 4z"/></svg>444.555.7812</li>
        <li><svg viewBox="0 0 20 20"><rect x="2" y="4" width="16" height="12"/><path d="M2 4l8 7 8-7"/></svg>info@VeridanStrategy.com</li>
        <li><svg viewBox="0 0 20 20"><circle cx="10" cy="10" r="8"/><path d="M2 10h16M10 2c-4 4-4 12 0 16M10 2c4 4 4 12 0 16"/></svg>www.veridanstrategy.com</li>
      </ul>
    </div>
  </section>
</body>
</html>
```